Website Update for Global Company - Solar Technology - GreenTech

We recently released our first version of our website kelvaro.com. However despite a longer process of developing the page, it is still missing the elements of a brilliant website. (Currently it looks dead and boring) We are having problems integrating our logo and want to create a more catching site. The task involves an updated and without changing most of main elements in the existing page. (Unless you can do it even better) The blue color needs to be kept but can be changed within the blue-spectrum. The logo text (KELVARO) must be better integrated in the site, however the main logo could be used in elements like we have tried with the background. The surface of the logo could be changed to 3D or metallic, or any other theme that would make the site more complete.
It would be good if some elements of the site could be used on business cards and invoices to keep the company identity.
Kelvaro is a new development company specialized in green energy and sustainable development. We do design, engineering, manufacturing, sourcing and other processes related to product development – both as consultants and for own products.
Keep the look of the site as professional as possible, and with a cooperate-looking style.

Link to existing page: www.kelvaro.com

Brief Update : After reviewing the designs we would like all new and current designers to make more bold designs that stands out from the rest. We do not like the standard layout that looks like any other cooperate homepage. We want a very unique and very lively page - with faded images and effects when hoovering like seen on our existing page. Try make all elements blend together, and use faded background images instead of just white color - or something else.

Make the site unique !

Industry/Entity Type

Solar Energy

Contact Information for Business Card

Owner/Founder/CEO : Tobias Haldrup Jessen
Company name: Kelvaro ApS
Email: tobias.haldrup@kelvaro-mail.dk
Phone: +45 61 87 34 09
Slogan Sustainable Development
Address: Hyldegade 18, 2
DK-5700 Svendborg, Denmark

Number of Pages Required

3 page

Font styles to use
Serif
Sans Serif

Colors
0555a3
85acd3
cedeed
3176b5
cee9f5
85cae6
0293ce
86cfc6
33b8a4

```html
<!DOCTYPE html>
<html lang="en">
<head>
<meta charset="utf-8">
<title>Kelvaro – Sustainable Development</title>
<link href="https://fonts.googleapis.com/css2?family=Open+Sans:wght@400;600;700&family=Raleway:wght@400;600;700;800&display=swap" rel="stylesheet">
<style>
:root{
  --blue:#1a9be0;
  --blue-dark:#0555a3;
  --blue-mid:#3176b5;
  --ink:#2b2f33;
  --muted:#7a8088;
  --line:#dfe3e7;
  --paper:#ffffff;
  --bg:#eef1f4;
  --dark:#1d2126;
  --darker:#14171b;
}
*{box-sizing:border-box;margin:0;padding:0}
html,body{width:1200px;height:2832px;overflow:hidden}
body{position:relative;background:var(--bg);font-family:"Open Sans",Arial,sans-serif;color:var(--ink)}
.abs{position:absolute}
h1,h2,h3,.nav,.logo{font-family:"Raleway",Arial,sans-serif}

/* hero */
.hero{left:0;top:0;width:1200px;height:740px;background:linear-gradient(180deg,#d9dde1 0%,#f4f5f6 40%,#e3e6e9 100%)}
.hero-photo{left:0;top:0;width:1200px;height:740px;background:radial-gradient(ellipse at 60% 35%,rgba(255,255,255,.9) 0%,rgba(200,205,210,.5) 45%,rgba(170,176,182,.4) 100%)}
.header{left:0;top:0;width:1200px;height:72px;background:rgba(255,255,255,.55)}
.logo{left:40px;top:18px;display:flex;align-items:center;gap:12px;font-size:34px;font-weight:800;letter-spacing:2px;color:#3a3f45}
.logo .mark{width:30px;height:30px;border-radius:50%;background:#3a3f45}
.nav{right:40px;top:22px;display:flex;gap:26px;font-size:12px;font-weight:700;letter-spacing:1px;color:#3a3f45}
.nav span{padding:6px 12px}
.nav .active{background:var(--blue);color:#fff;border-radius:3px}
.hero-title{left:0;top:262px;width:1200px;text-align:center;font-size:30px;font-weight:700;line-height:38px;color:var(--dark);letter-spacing:1px}
.service{top:520px;width:190px;height:190px;background:rgba(255,255,255,.55);border:1px solid rgba(255,255,255,.8);text-align:center}
.service .circle{width:112px;height:112px;border-radius:50%;background:var(--blue);margin:22px auto 10px;display:flex;align-items:center;justify-content:center;border:5px solid #fff;box-shadow:0 2px 8px rgba(0,0,0,.15)}
.service .label{font-size:14px;font-weight:600;color:var(--blue);letter-spacing:1px}
.plus{top:585px;width:40px;text-align:center;font-size:38px;color:#fff;font-weight:300}

/* features */
.feature{top:770px;width:536px;height:200px;background:var(--paper);box-shadow:0 1px 4px rgba(0,0,0,.08);display:flex}
.feature .ph{width:210px;height:176px;margin:12px}
.feature .body{padding:20px 18px 0 6px;flex:1}
.feature h3{font-size:15px;font-weight:700;color:var(--blue);margin-bottom:8px}
.feature p{font-size:11px;line-height:17px;color:var(--muted)}
.btn{display:inline-block;background:var(--blue);color:#fff;font-size:11px;font-weight:600;padding:7px 16px;border-radius:2px;margin-top:12px}

/* videos */
.videos{left:0;top:1012px;width:1200px;height:190px;background:linear-gradient(90deg,#1f242a,#33393f 50%,#1f242a)}
.videos h2{position:absolute;top:50px;width:100%;text-align:center;color:#fff;font-size:26px;font-weight:700;letter-spacing:1px}
.videos svg{position:absolute;left:578px;top:100px}

/* expertise grid */
.grid-bg{left:0;top:1240px;width:1200px;height:780px;background:linear-gradient(180deg,#e9edf1,#f5f6f8)}
.card{width:264px;height:290px;background:var(--paper);text-align:center;box-shadow:0 1px 3px rgba(0,0,0,.08)}
.card h3{font-size:17px;font-weight:700;color:var(--blue);line-height:21px;height:56px;padding-top:12px}
.card .icon{height:64px;display:flex;align-items:center;justify-content:center;margin-top:8px}
.card p{font-size:11px;line-height:16px;color:var(--muted);padding:18px 30px 0;height:90px}
.card .more{position:absolute;left:12px;right:12px;bottom:16px;height:26px;background:var(--blue);color:#fff;font-size:10px;font-weight:700;line-height:26px;letter-spacing:.5px}
.card.hl{background:var(--blue);top:1306px !important;height:310px}
.card.hl h3,.card.hl p{color:#fff}
.card.hl .more{background:#fff;color:var(--blue)}

/* cta */
.cta{left:0;top:2060px;width:1200px;height:160px;background:#1f4f7d}
.cta-photo{left:600px;top:2060px;width:600px;height:160px;background:linear-gradient(90deg,#1f4f7d,#6f8ea8 60%,#a9b7c3)}
.cta h2{position:absolute;left:180px;top:34px;font-size:26px;font-weight:600;color:#fff}
.cta .go{position:absolute;left:240px;top:92px;width:200px;height:34px;background:#fff;color:var(--dark);font-size:12px;font-weight:700;text-align:center;line-height:34px}

/* news */
.news{left:0;top:2240px;width:1200px;height:260px;background:var(--blue)}
.news h2{position:absolute;top:30px;width:100%;text-align:center;font-size:26px;font-weight:700;color:#fff;letter-spacing:1px}
.news-item{top:90px;width:352px;height:110px;background:#fff;display:flex;padding:18px}
.date{width:70px;height:70px;border:1px solid var(--line);text-align:center;font-weight:700;color:var(--ink);margin-right:14px;flex:none}
.date b{display:block;font-size:22px;padding-top:8px}
.date span{font-size:11px;color:var(--muted)}
.news-item h3{font-size:14px;font-weight:700;margin-bottom:6px}
.news-item p{font-size:11px;line-height:15px;color:var(--muted)}

/* social */
.social{left:0;top:2500px;width:1200px;height:232px;background:#f4f5f7}
.social h2{position:absolute;top:42px;width:100%;text-align:center;font-size:26px;font-weight:700;color:var(--blue);letter-spacing:1px}
.sbtn{top:112px;width:214px;height:48px;color:#fff;font-weight:700;font-size:17px;display:flex;align-items:center;justify-content:center;gap:10px;border-radius:2px}
.sbtn i{width:16px;height:16px;background:rgba(255,255,255,.85);border-radius:50%;display:inline-block}
.scount{top:172px;width:214px;text-align:center;font-size:11px;color:var(--muted)}

/* contact + footer */
.contact{left:0;top:2732px;width:1200px;height:50px;background:var(--dark);color:#fff;font-size:15px;display:flex;justify-content:center;align-items:center;gap:90px}
.contact span{display:flex;align-items:center;gap:10px}
.footer{left:0;top:2782px;width:1200px;height:50px;background:var(--darker)}
.footer .logo{top:12px;font-size:22px;color:#9aa0a6}
.footer .logo .mark{width:20px;height:20px;background:#9aa0a6}
.footer small{position:absolute;left:0;width:100%;top:18px;text-align:center;font-size:11px;color:#8a9096}
</style>
</head>
<body>

<section class="abs hero">
  <div class="abs hero-photo" role="img" aria-label="Photo of a hand touching floating transparent digital screens"></div>
  <header class="abs header">
    <div class="abs logo"><span class="mark"></span>KELVARO</div>
    <nav class="abs nav"><span class="active">HOME</span><span>EXPERTISE</span><span>APPROACH</span><span>CLIENTS</span><span>ABOUT</span><span>CONTACT</span></nav>
  </header>
  <h1 class="abs hero-title">WE PROVIDE COMPLETE SERVICES THROUGHOUT<br>THE PRODUCT DEVELOPMENT PROCESS</h1>

  <div class="abs service" style="left:48px"><div class="circle"><svg width="44" height="44" viewBox="0 0 24 24" fill="none" stroke="#fff" stroke-width="2"><path d="M5 3h10l4 4v14H5z"/><circle cx="10" cy="11" r="2"/><path d="M7 18l4-4 3 3 2-2 2 3"/></svg></div><div class="label">DESIGN</div></div>
  <div class="abs plus" style="left:263px">+</div>
  <div class="abs service" style="left:334px"><div class="circle"><svg width="44" height="44" viewBox="0 0 24 24" fill="none" stroke="#fff" stroke-width="2"><path d="M8 20V8a4 4 0 0 1 8 0v12M12 4v16"/></svg></div><div class="label">ENGINEERING</div></div>
  <div class="abs plus" style="left:559px">+</div>
  <div class="abs service" style="left:630px"><div class="circle"><svg width="44" height="44" viewBox="0 0 24 24" fill="#fff"><rect x="4" y="12" width="7" height="7"/><rect x="13" y="12" width="7" height="7"/><rect x="8.5" y="4" width="7" height="7"/></svg></div><div class="label">SOURCING</div></div>
  <div class="abs plus" style="left:855px">+</div>
  <div class="abs service" style="left:926px"><div class="circle"><svg width="44" height="44" viewBox="0 0 24 24" fill="none" stroke="#fff" stroke-width="2"><circle cx="9" cy="9" r="3"/><circle cx="16" cy="16" r="2.5"/><path d="M9 3v2M9 13v2M3 9h2M13 9h2M16 11v1.5M16 19.5V21M11 16h1.5M19.5 16H21"/></svg></div><div class="label">MANUFACTURING</div></div>
</section>

<article class="abs feature" style="left:48px">
  <div class="ph" role="img" aria-label="Photo of a woman working at a desk with a laptop" style="background:linear-gradient(135deg,#c9ced3,#8d959d)"></div>
  <div class="body"><h3>FEATURE INNOVATION</h3><p>Ideas shaped into working products, from first sketch to tested prototype. We guide every step with care and clear goals, keeping quality, cost and time in balance.</p><span class="btn">Read More</span></div>
</article>
<article class="abs feature" style="left:616px">
  <div class="ph" role="img" aria-label="Photo of a tablet lying on a desk" style="background:linear-gradient(135deg,#e3e6e9,#9aa3ab)"></div>
  <div class="body"><h3>OUR WORK</h3><p>A look at recent projects in green energy and sustainable design, built together with partners who share our drive for smart, lasting solutions.</p><span class="btn">Read More</span></div>
</article>

<section class="abs videos" role="img" aria-label="Dark faded background photo of a workshop">
  <h2>PROJECT VIDEOS</h2>
  <svg width="44" height="44" viewBox="0 0 44 44"><circle cx="22" cy="22" r="20" fill="none" stroke="#fff" stroke-width="3"/><path d="M18 14l12 8-12 8z" fill="#fff"/></svg>
</section>

<div class="abs grid-bg"></div>

<div class="abs card" style="left:48px;top:1320px"><h3>Focused<br>Innovation</h3><div class="icon"><svg width="60" height="44" viewBox="0 0 30 22" fill="#2b2f33"><circle cx="15" cy="6" r="4"/><path d="M8 20c0-5 3-8 7-8s7 3 7 8z"/><circle cx="6" cy="8" r="3"/><path d="M0 20c0-4 2-6 6-6l1 6z"/><circle cx="24" cy="8" r="3"/><path d="M30 20c0-4-2-6-6-6l-1 6z"/></svg></div><p>Clear focus on the problem lets us find new ideas that truly move a product forward.</p><div class="more">READ MORE</div></div>
<div class="abs card hl" style="left:328px"><h3>Industrial<br>Design</h3><div class="icon"><svg width="44" height="52" viewBox="0 0 22 26" fill="none" stroke="#fff" stroke-width="2"><path d="M2 1h12l6 6v18H2z"/><circle cx="9" cy="11" r="2.5"/><path d="M4 21l5-5 3 3 2-2 4 4"/></svg></div><p>Form and function joined in designs that are easy to build, use and love.</p><div class="more">READ MORE</div></div>
<div class="abs card" style="left:608px;top:1320px"><h3>Science &amp;<br>Technology</h3><div class="icon"><svg width="48" height="48" viewBox="0 0 24 24" fill="none" stroke="#2b2f33" stroke-width="2.2"><circle cx="12" cy="12" r="10"/><circle cx="12" cy="12" r="4"/><path d="M5 5l4 4M19 5l-4 4M5 19l4-4M19 19l-4-4"/></svg></div><p>Sound research and modern tools give each project a solid technical base.</p><div class="more">READ MORE</div></div>
<div class="abs card" style="left:888px;top:1320px"><h3>We Are Looking For<br>New Problem To Solve</h3><div class="icon"><svg width="30" height="52" viewBox="0 0 14 26" fill="#2b2f33"><circle cx="7" cy="3" r="3"/><path d="M2 7h10v9h-2v10H8v-8H6v8H4V16H2z"/></svg></div><p>Bring us your challenge and we will help turn it into a working answer.</p><div class="more">READ MORE</div></div>

<div class="abs card" style="left:48px;top:1680px"><h3>Prototype<br>Development</h3><div class="icon"><svg width="48" height="48" viewBox="0 0 24 24" fill="#2b2f33"><circle cx="12" cy="12" r="3"/><circle cx="4" cy="5" r="2.5"/><circle cx="20" cy="5" r="2.5"/><circle cx="12" cy="21" r="2.5"/><path d="M5 6l6 5M19 6l-6 5M12 14v5" stroke="#2b2f33" stroke-width="2"/></svg></div><p>Fast, hands-on prototypes that let you test ideas early and save cost later.</p><div class="more">READ MORE</div></div>
<div class="abs card" style="left:328px;top:1680px"><h3>Electrical<br>Engineering</h3><div class="icon"><svg width="48" height="48" viewBox="0 0 24 24" fill="none" stroke="#2b2f33" stroke-width="2.6" stroke-linecap="round"><path d="M4 20l9-9"/><path d="M14 4a5 5 0 0 0 6 6l-3 3-6-6z" fill="#2b2f33"/></svg></div><p>Circuits, power and control systems built for safe and efficient products.</p><div class="more">READ MORE</div></div>
<div class="abs card" style="left:608px;top:1680px"><h3>Manufacturing<br>Development</h3><div class="icon"><svg width="52" height="48" viewBox="0 0 26 24" fill="none" stroke="#2b2f33" stroke-width="2.4"><circle cx="9" cy="10" r="4"/><circle cx="19" cy="17" r="3"/><path d="M9 3v2M9 15v2M2 10h2M14 10h2M19 11v2M19 21v2M13 17h2M23 17h2"/></svg></div><p>From small runs to full series, we set up production that scales well.</p><div class="more">READ MORE</div></div>
<div class="abs card" style="left:888px;top:1680px"><h3>Maker Space<br>Coming Soon</h3><div class="icon"><svg width="48" height="48" viewBox="0 0 24 24" fill="#2b2f33"><rect x="3" y="4" width="8" height="7"/><rect x="13" y="4" width="8" height="7"/><rect x="8" y="13" width="8" height="7"/></svg></div><p>A shared workshop for makers, students and startups opens here soon.</p><div class="more">READ MORE</div></div>

<section class="abs cta">
  <h2>Manufacturing Development</h2>
  <div class="go">LET'S GET STARTED</div>
</section>
<div class="abs cta-photo" role="img" aria-label="Faded photo of an engineer reviewing technical plans"></div>

<section class="abs news">
  <h2>IN THE NEWS</h2>
  <div class="abs news-item" style="left:48px"><div class="date"><b>29</b><span>AUG</span></div><div><h3>Launch of website</h3><p>Our new site is live with news, projects and ways to reach us.</p></div></div>
  <div class="abs news-item" style="left:424px"><div class="date"><b>29</b><span>AUG</span></div><div><h3>First project initiated</h3><p>Work has begun on our first solar product with a local partner.</p></div></div>
  <div class="abs news-item" style="left:800px"><div class="date"><b>29</b><span>AUG</span></div><div><h3>Establishment of Kelvaro ApS</h3><p>The company is founded to drive green and sustainable development.</p></div></div>
</section>

<section class="abs social">
  <h2>FOLLOW US TO STAY IN TOUCH</h2>
  <div class="abs sbtn" style="left:72px;background:#3b5b9a"><i></i>Pagebook</div>
  <div class="abs sbtn" style="left:350px;background:#2aa3e0"><i></i>Chirper</div>
  <div class="abs sbtn" style="left:628px;background:#1d6aa5"><i></i>WorkLink</div>
  <div class="abs sbtn" style="left:906px;background:#d3263f"><i></i>Snapgram</div>
  <div class="abs scount" style="left:72px">2230 likes</div>
  <div class="abs scount" style="left:350px">2230 Followers</div>
  <div class="abs scount" style="left:628px">2230 Followers</div>
  <div class="abs scount" style="left:906px">2230 Followers</div>
</section>

<div class="abs contact">
  <span><svg width="16" height="16" viewBox="0 0 24 24" fill="#fff"><path d="M6 2l4 4-2 3c1 3 4 6 7 7l3-2 4 4-3 4C10 22 2 14 2 5z"/></svg>123.456.7890</span>
  <span><svg width="18" height="14" viewBox="0 0 24 18" fill="none" stroke="#fff" stroke-width="2"><rect x="1" y="1" width="22" height="16"/><path d="M1 1l11 9 11-9"/></svg>info@companyname.com</span>
</div>
<footer class="abs footer">
  <div class="abs logo"><span class="mark"></span>KELVARO</div>
  <small>All Rights Reserved. Copyright © 2016 Kelvaro</small>
</footer>

</body>
</html>
```